Business Card Design Quokka Celebration Co

on the front i would like to see the logo and my contact details. on the back i would like it to include the 3 parts to the business party planning, party hire and party supplies also with a line at the bottom (or white space) to write their appointment details.

Target Market(s)

mums and corporates

Industry/Entity Type

Business

Requirements
Must have
• logo and contact details which are: Name: Janelle, Phone: 0417263954, email: jan@quokkaevents.com.au, Website: www.quokkaevents.com.au,

```html
<!DOCTYPE html>
<html lang="en">
<head>
<meta charset="utf-8">
<title>Quokka Celebration Co — Business Card</title>
<link rel="stylesheet" href="https://fonts.googleapis.com/css2?family=Lato:wght@300;400;700;900&display=swap">
<style>
  :root {
    --page: #ececef;
    --card: #ffffff;
    --purple: #5b45a8;
    --purple-light: #7e6bc0;
    --cyan: #22b6dc;
    --yellow: #f6c21c;
    --magenta: #c23d9c;
    --ink: #4a4a55;
    --rule: #d4d4da;
    --line: #3f2f9a;
  }
  * { box-sizing: border-box; margin: 0; padding: 0; }
  html, body { width: 1200px; height: 840px; overflow: hidden; }
  body {
    background: var(--page);
    font-family: "Lato", sans-serif;
    color: var(--ink);
    display: flex;
    align-items: center;
    justify-content: center;
    gap: 50px;
  }
  .card {
    position: relative;
    width: 525px;
    height: 300px;
    background: var(--card);
    box-shadow: 0 6px 24px rgba(40, 30, 80, 0.14);
    overflow: hidden;
  }

  /* Front */
  .card-front::after {
    content: "";
    position: absolute;
    left: 0; right: 0; bottom: 0;
    height: 14px;
    background: var(--purple);
  }
  .brand {
    position: absolute;
    left: 28px; top: 26px;
    display: flex;
    align-items: center;
    gap: 10px;
  }
  .brand-mark {
    width: 30px; height: 30px;
    border-radius: 50%;
    background: var(--cyan);
  }
  .brand-name {
    font-size: 22px;
    font-weight: 900;
    color: var(--purple);
    letter-spacing: 0.5px;
  }
  .name-tag {
    position: absolute;
    left: 28px; top: 80px;
    width: 200px; height: 40px;
    background: var(--cyan);
    border-radius: 0 4px 4px 0;
    color: #fff;
    font-size: 22px;
    font-weight: 700;
    letter-spacing: 2px;
    display: flex;
    align-items: center;
    justify-content: center;
  }
  .contacts {
    position: absolute;
    left: 28px; right: 28px; top: 142px;
    list-style: none;
  }
  .contact {
    display: flex;
    align-items: flex-end;
    gap: 14px;
    height: 42px;
  }
  .contact-icon {
    flex: none;
    width: 32px; height: 30px;
    border-radius: 3px;
    display: flex;
    align-items: center;
    justify-content: center;
  }
  .contact-icon svg { width: 14px; height: 14px; fill: #fff; }
  .icon-phone { background: var(--yellow); }
  .icon-mail { background: var(--magenta); }
  .icon-web { background: var(--cyan); }
  .contact-text {
    flex: 1;
    font-size: 15px;
    padding-bottom: 5px;
    border-bottom: 1px solid var(--rule);
    letter-spacing: 0.3px;
  }

  /* Back */
  .services {
    position: absolute;
    left: 42px; right: 42px; top: 0;
    height: 120px;
    background: linear-gradient(110deg, var(--purple-light), var(--purple));
    border-radius: 0 0 6px 6px;
    color: #fff;
    text-align: center;
    display: flex;
    flex-direction: column;
    justify-content: center;
    font-size: 20px;
    font-weight: 300;
    letter-spacing: 0.5px;
    line-height: 1.3;
  }
  .services strong { font-weight: 900; }
  .appointment-label {
    position: absolute;
    left: 0; right: 0; top: 140px;
    text-align: center;
    font-size: 9px;
    letter-spacing: 1px;
    color: var(--line);
  }
  .appointment-lines {
    position: absolute;
    left: 42px; right: 42px; top: 172px;
    list-style: none;
  }
  .appointment-lines li {
    height: 28px;
    border-bottom: 1.5px solid var(--line);
  }
</style>
</head>
<body>
  <section class="card card-front" aria-label="Card front">
    <div class="brand">
      <span class="brand-mark"></span>
      <span class="brand-name">Quokka Celebration Co</span>
    </div>
    <div class="name-tag">JANELLE</div>
    <ul class="contacts">
      <li class="contact">
        <span class="contact-icon icon-phone">
          <svg viewBox="0 0 24 24"><path d="M6.6 10.8a15.1 15.1 0 0 0 6.6 6.6l2.2-2.2a1 1 0 0 1 1-.25 11.4 11.4 0 0 0 3.6.57 1 1 0 0 1 1 1V20a1 1 0 0 1-1 1A17 17 0 0 1 3 4a1 1 0 0 1 1-1h3.5a1 1 0 0 1 1 1c0 1.25.2 2.45.57 3.57a1 1 0 0 1-.25 1z"/></svg>
        </span>
        <span class="contact-text">0417263954</span>
      </li>
      <li class="contact">
        <span class="contact-icon icon-mail">
          <svg viewBox="0 0 24 24"><path d="M2 5h20v14H2z M4 7v.5l8 5 8-5V7z" fill-rule="evenodd"/></svg>
        </span>
        <span class="contact-text">jan@quokkaevents.com.au</span>
      </li>
      <li class="contact">
        <span class="contact-icon icon-web">
          <svg viewBox="0 0 24 24"><path d="M12 2a7 7 0 0 0-7 7c0 5.2 7 13 7 13s7-7.8 7-13a7 7 0 0 0-7-7zm0 9.5A2.5 2.5 0 1 1 12 6.5a2.5 2.5 0 0 1 0 5z"/></svg>
        </span>
        <span class="contact-text">www.quokkaevents.com.au</span>
      </li>
    </ul>
  </section>

  <section class="card card-back" aria-label="Card back">
    <div class="services">
      <p><strong>PARTY</strong> PLANNING</p>
      <p><strong>PARTY</strong> HIRE AND <strong>PARTY</strong> SUPPLIES</p>
    </div>
    <p class="appointment-label">APPOINTMENT DETAILS</p>
    <ul class="appointment-lines">
      <li></li><li></li><li></li><li></li>
    </ul>
  </section>
</body>
</html>
```